Road Sign at our office 84 in X 48 in - Small Billboard

Kestrel Electrical
Electrical & Lighting Services

- we need a sign design for our small business/company based in Calhoun, GA called Kestrel Electrical - "our mission is to provide Northwest Georgia with dependable, high-quality electrical services that prioritize safety, integrity, and long-term reliability. As a woman-owned business with over 25 years of experience, we are committed to delivering exceptional workmanship and personalized service for every commercial, residential, and industrial project we undertake. We stand behind our work with a lifetime warranty—because your trust is our most powerful connection."

display logo, phone number, and open to other ideas without being cluttered, maybe instead of full website address, just use @kstelectrical and it will send them to all of our website and socials...

it needs to be easy to read as they drive down the road
this is a place where people may be traveling at high speeds, make sure it's easy to see and understand at a glance.
It will be hanging 20-24ft from the ground. Like a small billboard.

https://kstelectricalservices.example/

Industry/Entity Type

Electrical Contractor

Requirements
Nice to have
• match the look and feel of website and socials

```html
<!DOCTYPE html>
<html lang="en">
<head>
<meta charset="utf-8">
<title>Kestrel Electrical – Road Sign</title>
<link rel="stylesheet" href="https://fonts.googleapis.com/css2?family=Montserrat:wght@700&family=Oswald:wght@500&display=swap">
<style>
  :root {
    --page-bg: #e6e6e6;
    --sign-white: #ffffff;
    --brand-orange: #e84e1b;
    --brand-amber: #f29100;
    --ink: #0b0b0b;
    --text-light: #ffffff;
  }
  * { margin: 0; padding: 0; box-sizing: border-box; }
  html, body {
    width: 1200px;
    height: 1157px;
    overflow: hidden;
    background: var(--page-bg);
  }
  .sign {
    position: absolute;
    left: 0;
    top: 322px;
    width: 1200px;
    height: 513px;
    background: var(--sign-white);
    overflow: hidden;
  }
  .sign-wave {
    position: absolute;
    inset: 0;
    width: 1200px;
    height: 513px;
  }
  .wave-accent { fill: var(--brand-amber); }
  .wave-band { fill: var(--brand-orange); }
  .brand-mark {
    position: absolute;
    left: 58px;
    top: 92px;
    width: 150px;
    height: 150px;
    border-radius: 50%;
    background: var(--brand-amber);
  }
  .brand-name {
    position: absolute;
    left: 246px;
    top: 96px;
    font-family: "Montserrat", sans-serif;
    font-weight: 700;
    color: var(--ink);
    line-height: 1;
  }
  .brand-name .word-main {
    display: block;
    font-size: 122px;
    letter-spacing: -2px;
  }
  .brand-name .word-trade {
    display: block;
    margin-top: 18px;
    font-size: 42px;
    letter-spacing: 25px;
    text-transform: uppercase;
  }
  .contact-line {
    position: absolute;
    left: 0;
    right: 0;
    bottom: 18px;
    text-align: center;
    font-family: "Oswald", sans-serif;
    font-weight: 500;
    font-size: 82px;
    letter-spacing: 3px;
    color: var(--text-light);
    text-transform: uppercase;
    line-height: 1;
  }
  .contact-line .divider { margin: 0 26px; }
</style>
</head>
<body>
  <main class="sign">
    <svg class="sign-wave" viewBox="0 0 1200 513" aria-hidden="true">
      <path class="wave-accent" d="M0,513 L0,405 C300,330 700,368 890,250 C1040,160 1140,80 1180,0 L1200,0 L1200,513 Z"/>
      <path class="wave-band" d="M0,513 L0,420 C300,346 710,384 905,262 C1055,170 1160,90 1200,12 L1200,513 Z"/>
    </svg>

    <div class="brand-mark" aria-hidden="true"></div>
    <h1 class="brand-name">
      <span class="word-main">Kestrel</span>
      <span class="word-trade">Electrical</span>
    </h1>

    <p class="contact-line">
      <span class="phone">706-555-0148</span><span class="divider">|</span><span class="handle">@kstelectrical</span>
    </p>
  </main>
</body>
</html>
```